Design for a 4 screens iOS and Android app - "VelidMetra"

The app allows you to track your car gasoline refill ...
We need a design for the 4 screens of the app:
a) 1 form with 3 fields.
b) 1 simple list view
c) 1 summary view
d) 1 text page
2 "alerts" items are also to be designed.
No specific guidelines, nor logo or whatever.
It will be a free app distributed on iOS and Androïd.
We just want to make it looking nice & very usable for end users.
Target Market(s)
B2C app
Industry/Entity Type
Android

```html
<!DOCTYPE html>
<html lang="en">
<head>
<meta charset="utf-8">
<title>VelidMetra – app screens</title>
<link rel="stylesheet" href="https://fonts.googleapis.com/css2?family=Roboto:wght@400;700&display=swap">
<style>
:root{
  --stage:#2ef2ea;
  --nav:#0a86f7;
  --nav-line:#5fb0fb;
  --sky-top:#7ec1ea;
  --sky-mid:#7cbde8;
  --sky-low:#2a6cc0;
  --brand:#0b84f5;
  --ink-blue:#1a7fd8;
  --row-tint:#d8edfb;
  --white:#ffffff;
  --field-text:#8a8f96;
  --error:#e8472b;
}
*{margin:0;padding:0;box-sizing:border-box}
html,body{width:1200px;height:981px;overflow:hidden;background:var(--stage)}
body{font-family:"Roboto",Arial,sans-serif}
.board{position:relative;width:1278px;height:1045px;transform:scale(.939);transform-origin:0 0}
.screen{position:absolute;width:281px;height:500px;overflow:hidden;background:var(--white)}
.screen.sky{background:linear-gradient(180deg,var(--sky-top) 0%,var(--sky-mid) 52%,var(--sky-low) 100%)}
.nav{position:absolute;left:0;top:0;width:100%;height:45px;background:var(--nav);display:flex}
.nav .tab{flex:1;display:flex;align-items:center;justify-content:center;border-left:1px solid var(--nav-line)}
.nav .tab:first-child{border-left:none}
.field{position:absolute;left:36px;width:209px;height:34px;border-radius:10px;background:var(--white);font-size:14px;color:var(--field-text);padding-left:20px;line-height:34px}
.field.error{color:var(--error)}
.field .x{position:absolute;right:18px;top:10px}
.btn{position:absolute;left:82px;width:118px;height:35px;border-radius:8px;background:var(--brand);color:var(--white);font-weight:700;font-size:15px;text-align:center;line-height:35px}
.about{position:absolute;left:0;width:100%;top:444px;text-align:center;color:var(--white);font-size:12px}
.veil{position:absolute;inset:0;background:rgba(200,225,245,.35)}
.dialog{position:absolute;left:0;top:201px;width:100%;height:93px;background:var(--white);text-align:center}
.dialog h2{font-size:14px;color:var(--brand);font-weight:700;margin-top:23px}
.dialog .ok{display:inline-block;margin-top:10px;width:71px;height:23px;border-radius:5px;background:var(--brand);color:var(--white);font-size:11px;font-weight:700;line-height:23px}
.list{position:absolute;top:45px;left:0;width:100%}
.list h3{height:45px;line-height:45px;text-align:center;color:var(--ink-blue);font-size:14px;font-weight:700;background:var(--white);word-spacing:3px}
.summary{background:var(--row-tint);height:135px;padding:24px 16px 0 15px}
.summary p{display:flex;justify-content:space-between;color:var(--ink-blue);font-size:14px;height:24px}
.entry{background:var(--row-tint);height:67px;display:flex;align-items:center;justify-content:space-between;padding:0 15px 0 17px;color:var(--ink-blue);font-size:14px}
.page{position:absolute;top:45px;left:0;width:100%;padding:37px 20px 0 21px;color:var(--white)}
.page h2{text-align:center;font-size:14px;font-weight:700;margin-bottom:12px}
.page p{font-size:12px;line-height:14px;text-align:justify}
</style>
</head>
<body>
<svg width="0" height="0" style="position:absolute">
  <defs>
    <symbol id="i-add" viewBox="0 0 20 20"><path d="M10 1v18M1 10h18" stroke="#fff" stroke-width="2"/></symbol>
    <symbol id="i-list" viewBox="0 0 26 18"><g fill="#fff"><circle cx="1.5" cy="2" r="1.5"/><circle cx="1.5" cy="9" r="1.5"/><circle cx="1.5" cy="16" r="1.5"/></g><path d="M6 2h20M6 9h20M6 16h20" stroke="#fff" stroke-width="2"/></symbol>
    <symbol id="i-chart" viewBox="0 0 24 18"><path d="M1 0v17h23" stroke="#fff" stroke-width="2" fill="none"/><path d="M3 16V9l4-5 5 5 4-3 6 6v4z" fill="#fff"/></symbol>
    <symbol id="i-clear" viewBox="0 0 14 14"><circle cx="7" cy="7" r="6" fill="none" stroke="#e8472b" stroke-width="1"/><path d="M4.5 4.5l5 5M9.5 4.5l-5 5" stroke="#e8472b" stroke-width="1"/></symbol>
  </defs>
</svg>

<div class="board">

  <!-- Form -->
  <section class="screen sky" style="left:168px;top:21px">
    <nav class="nav"><span class="tab"><svg width="20" height="20"><use href="#i-add"/></svg></span><span class="tab"><svg width="26" height="18"><use href="#i-list"/></svg></span><span class="tab"><svg width="24" height="18"><use href="#i-chart"/></svg></span></nav>
    <div class="field" style="top:151px">127500</div>
    <div class="field" style="top:201px">LITRES</div>
    <div class="field" style="top:249px">PRICE</div>
    <div class="btn" style="top:330px">Save</div>
    <div class="about">About us</div>
  </section>

  <!-- Form with errors -->
  <section class="screen sky" style="left:497px;top:21px">
    <nav class="nav"><span class="tab"><svg width="20" height="20"><use href="#i-add"/></svg></span><span class="tab"><svg width="26" height="18"><use href="#i-list"/></svg></span><span class="tab"><svg width="24" height="18"><use href="#i-chart"/></svg></span></nav>
    <div class="field" style="top:151px">127500</div>
    <div class="field error" style="top:201px">xyz<svg class="x" width="14" height="14"><use href="#i-clear"/></svg></div>
    <div class="field error" style="top:249px">xyz<svg class="x" width="14" height="14"><use href="#i-clear"/></svg></div>
    <div class="btn" style="top:330px">Save</div>
    <div class="about">About us</div>
  </section>

  <!-- Saved alert -->
  <section class="screen sky" style="left:827px;top:21px">
    <nav class="nav"><span class="tab"><svg width="20" height="20"><use href="#i-add"/></svg></span><span class="tab"><svg width="26" height="18"><use href="#i-list"/></svg></span><span class="tab"><svg width="24" height="18"><use href="#i-chart"/></svg></span></nav>
    <div class="field" style="top:151px">127500</div>
    <div class="btn" style="top:330px">Save</div>
    <div class="about">About us</div>
    <div class="veil"></div>
    <div class="dialog"><h2>Data saved</h2><span class="ok">OK</span></div>
  </section>

  <!-- Summary -->
  <section class="screen" style="left:168px;top:531px">
    <nav class="nav"><span class="tab"><svg width="20" height="20"><use href="#i-add"/></svg></span><span class="tab"><svg width="26" height="18"><use href="#i-list"/></svg></span><span class="tab"><svg width="24" height="18"><use href="#i-chart"/></svg></span></nav>
    <div class="list">
      <h3>February 2016</h3>
      <div class="summary"><p><span>Total cost</span><span>570€</span></p><p><span>Mileage</span><span>7500 km</span></p><p><span>Full tanks</span><span>11</span></p><p><span>Consumption</span><span>6,5 l</span></p></div>
      <h3>January 2016</h3>
      <div class="summary"><p><span>Total cost</span><span>241€</span></p><p><span>Mileage</span><span>2770 km</span></p><p><span>Full tanks</span><span>4</span></p><p><span>Consumption</span><span>6,2 l</span></p></div>
      <h3>December 2015</h3>
      <div class="summary"><p><span>Total cost</span><span>180€</span></p><p><span>Mileage</span><span>2100 km</span></p></div>
    </div>
  </section>

  <!-- Refill list -->
  <section class="screen" style="left:497px;top:531px">
    <nav class="nav"><span class="tab"><svg width="20" height="20"><use href="#i-add"/></svg></span><span class="tab"><svg width="26" height="18"><use href="#i-list"/></svg></span><span class="tab"><svg width="24" height="18"><use href="#i-chart"/></svg></span></nav>
    <div class="list">
      <h3>15 Feb. 2016 14:24</h3>
      <div class="entry"><span>127500 km</span><span>49,88 l</span><span>47,25€</span></div>
      <h3>08 Feb. 2016 13:14</h3>
      <div class="entry"><span>126500 km</span><span>50,11 l</span><span>49,75€</span></div>
      <h3>01 Feb. 2016 11:17</h3>
      <div class="entry"><span>125500 km</span><span>42,50 l</span><span>44,70€</span></div>
      <h3>27 Jan. 2016 12:21</h3>
      <div class="entry"><span>123500 km</span><span>49,88 l</span><span>47,25€</span></div>
      <h3></h3>
    </div>
  </section>

  <!-- Text page -->
  <section class="screen sky" style="left:826px;top:531px">
    <nav class="nav"><span class="tab"><svg width="20" height="20"><use href="#i-add"/></svg></span><span class="tab"><svg width="26" height="18"><use href="#i-list"/></svg></span><span class="tab"><svg width="24" height="18"><use href="#i-chart"/></svg></span></nav>
    <div class="page">
      <h2>Lorem ipsum</h2>
      <p>Lorem ipsum dolor sit amet, consectetur adipisicing elit, sed do eiusmod tempor incididunt ut labore et dolore magna aliqua. Ut enim ad minim veniam, quis nostrud exercitation ullamco laboris nisi ut aliquip ex ea commodo consequat. Duis aute irure dolor in reprehenderit in voluptate velit esse cillum dolore eu fugiat nulla pariatur. Excepteur sint occaecat cupidatat non proident, sunt in culpa qui officia deserunt mollit anim id est laborum. Sed ut perspiciatis unde omnis iste natus error sit voluptatem accusantium doloremque laudantium, totam rem aperiam, eaque ipsa quae ab illo inventore veritatis et quasi architecto beatae vitae dicta sunt explicabo.</p>
    </div>
    <div class="btn" style="top:389px">Close</div>
  </section>

</div>
</body>
</html>
```